Chai Tea Company needs a Tea Packaging Box Design

Tea Packaging
Dimensions of the Tea Packaging Box: Height 13 cm; Width 8.5 cm; Depth 7 cm
Individual Teabag Packet/ Sachet: Width 6.5 cm; Length 8.25 cm
We are looking for a new tea packaging design, for our tea business. The material of the box is cardboard. We are also looking for a design that will be on each individual tea bag sachet/packet that goes into the box. This design will be very similar to what you design for the tea packaging box.
Product Info:
Our tea company is called “Velmora Leaf”. We sell two types of Chai Tea, once called “Velmora Gold” and one called “Velmora Bloom”. The Velmora Gold has caffeine, while the Velmora Bloom is Naturally Caffeine Free. The Velmora Gold has a black tea base, while the Velmora Bloom has a Rooibos tea base. We will need two tea packaging designs, one for each Chai Tea flavour. The designs for both the teas can be similar, but make sure that you can easily distinguish one from the other (example: make them have different colours or pictures). Both the chai teas, come from the same product line.
Tea Packaging Design:
We are looking for high end tea packaging. We produce high quality teas, and we would like to portray this in our tea packaging. Our teas are made with no artificial flavourings, natural flavourings, or preservatives, so we would also like a natural, organic, high quality look to our tea packaging. Our current logo is a llama. It would be great if you could make the current logo more polished and well made. If you feel that the llama is not well suited or you would like to design the llama differently, we are open to your creative ideas.
General Basic Info:
Keep in mind, we will have both English and French writing on the tea packaging. You do not need to worry about the French writing (we will do the translation), just make sure there is room for it. However, if you feel that you are capable and knowledgeable of incorporating both French and English language into the tea packaging that would be of great help and value.
Back of the Box:
- Will have ingredients and brewing instructions. Basic brewing instructions are: “Add hot water to teabag. Steep for 5-7 minutes, depending on strength preferred. Add milk and your choice of sweetener. Enjoy! See inside panel of box for more detailed instructions”. (The basic brewing instructions, can further be polished or written in a more creative or professional manner).
Front of the Box:
- Will have company name, type of tea, little description of the tea
- 18 teabags
- 54 g (1.9 OZ)
- Should state that this is a product of Alberta, Canada.
Side of the Box:
Any creative wording, slogan, or description about the tea, or whatever you feel would be good on the side of the box.
On the inside flap of the side of the box, there will be detailed instructions on how to brew the tea. These will be different from the simplified brewing instructions on the back of the box. I have attached the advanced brewing instructions as a file. These instructions can further be simplified or reduced to make it easier and cleaner for the consumers to read.
Individual Tea Sachets/ Packets
- These will have a matching look and design of the tea box packaging, except on a smaller scale. Each individual sachet will have the company name, type of tea, little description of the tea in the front of the sachet, while the back will contain the ingredients, and basic brewing instructions.
I have attached a few files, with the dimensions, ingredients, detailed brewing directions, and current logo of the business.
If you have any questions, about the design or packaging please let me know. The winning designer will be required to do a few additional tweaks to finalize the product. Thank you for your time and happy designing!

```html
<!DOCTYPE html>
<html lang="en">
<head>
<meta charset="utf-8">
<title>Velmora Leaf – Tea Packaging</title>
<link href="https://fonts.googleapis.com/css2?family=Courgette&family=Roboto+Condensed:wght@400&display=swap" rel="stylesheet">
<style>
  :root {
    --bg: #f3f0ea;
    --white: #ffffff;
    --band: #4d3f38;
    --band-text: #f4efe8;
    --gold-light: #f0901f;
    --gold-mid: #d9521a;
    --gold-deep: #8a2212;
    --gold-badge: #e8781c;
    --bloom-light: #e6e326;
    --bloom-mid: #b7bd1a;
    --bloom-deep: #7c8314;
    --bloom-badge: #b9c41e;
    --ink: #3b3330;
    --ink-soft: #6d625c;
    --accent-red: #c2281c;
    --heading-cream: #f1dfa6;
  }
  * { box-sizing: border-box; margin: 0; padding: 0; }
  html, body { width: 1200px; height: 1000px; overflow: hidden; background: var(--bg); }
  .canvas { position: relative; width: 1200px; height: 1000px; background: var(--bg); }

  .flavour--gold  { --light: var(--gold-light);  --mid: var(--gold-mid);  --deep: var(--gold-deep);  --badge: var(--gold-badge); }
  .flavour--bloom { --light: var(--bloom-light); --mid: var(--bloom-mid); --deep: var(--bloom-deep); --badge: var(--bloom-badge); }

  .panel { position: absolute; top: 50px; height: 468px; background: var(--white); overflow: hidden;
           box-shadow: 0 2px 10px rgba(60,40,30,.12); }
  .panel--side { left: 148px; width: 252px; border-right: 1px solid rgba(0,0,0,.08); }
  .panel--front-gold { left: 400px; width: 306px; }
  .panel--front-bloom { left: 746px; width: 306px; }

  .stripe { position: absolute; top: 0; bottom: 0; width: 56px;
            background: linear-gradient(180deg, var(--light) 0%, var(--mid) 55%, var(--deep) 100%); }
  .stripe--left { left: 0; }
  .stripe--right { right: 0; }

  .brand-mark { position: absolute; top: 46px; left: 0; right: 0; display: flex; align-items: center;
                justify-content: center; gap: 6px; font-family: "Roboto Condensed", sans-serif;
                font-size: 14px; color: var(--band); letter-spacing: .5px; }
  .brand-mark__dot { width: 10px; height: 10px; border-radius: 50%; background: var(--band); }

  .band { position: absolute; left: 0; right: 0; top: 128px; height: 78px; background: var(--band);
          color: var(--band-text); text-align: center; padding-top: 14px; }
  .band__name { font-family: "Roboto Condensed", sans-serif; font-weight: 400; font-size: 28px;
                letter-spacing: .5px; line-height: 1; }
  .band__tagline { font-family: "Roboto Condensed", sans-serif; font-weight: 400; font-size: 13px;
                   margin-top: 8px; letter-spacing: .3px; }

  .splash { position: absolute; top: 222px; left: 74px; width: 220px; height: 176px;
            border-radius: 60% 40% 55% 45% / 50% 60% 40% 50%;
            background: radial-gradient(ellipse at 60% 40%, var(--light) 0%, var(--mid) 55%, rgba(255,255,255,0) 80%); }

  .badge { position: absolute; left: 18px; top: 292px; width: 112px; height: 112px; border-radius: 50%;
           background: var(--badge); border: 4px solid var(--white); box-shadow: 0 0 0 2px var(--deep);
           color: var(--white); text-align: center; display: flex; flex-direction: column;
           justify-content: center; font-family: "Courgette", cursive; }
  .badge__name { font-size: 19px; line-height: 1.05; }
  .badge__count { font-size: 11px; margin-top: 4px; border-top: 1px solid rgba(255,255,255,.7);
                  padding-top: 3px; margin-left: 14px; margin-right: 14px; }

  .net { position: absolute; top: 416px; left: 56px; right: 56px; text-align: center;
         font-family: "Roboto Condensed", sans-serif; color: var(--ink); font-size: 10px; line-height: 1.5; }

  .side__intro { position: absolute; top: 22px; left: 20px; right: 20px; font-family: "Roboto Condensed", sans-serif;
                 font-size: 9.5px; line-height: 1.45; color: var(--accent-red); }
  .side__band { padding-top: 18px; }
  .side__heading { font-family: "Courgette", cursive; font-weight: 400; font-size: 15px; color: var(--heading-cream);
                   text-align: left; padding: 0 18px; }
  .side__sub { font-family: "Roboto Condensed", sans-serif; font-size: 9.5px; color: var(--band-text);
               text-align: left; padding: 4px 18px 0; opacity: .85; }
  .side__body { position: absolute; top: 228px; left: 20px; right: 20px; font-family: "Roboto Condensed", sans-serif;
                font-size: 9.5px; line-height: 1.5; color: var(--ink-soft); }
  .side__body p + p { margin-top: 12px; }

  .sachet { position: absolute; top: 600px; width: 297px; height: 234px; background: var(--white);
            overflow: hidden; box-shadow: 0 2px 10px rgba(60,40,30,.12); }
  .sachet--bloom { left: 148px; }
  .sachet--gold { left: 485px; }
  .sachet .stripe { width: 96px; }
  .sachet .brand-mark { top: 16px; left: auto; right: 0; width: 96px; font-size: 10px; color: var(--white); }
  .sachet .brand-mark__dot { width: 7px; height: 7px; background: var(--white); }
  .sachet .band { top: 44px; height: 54px; padding-top: 10px; }
  .sachet .band__name { font-size: 19px; }
  .sachet .band__tagline { font-size: 10px; margin-top: 5px; }
  .sachet .splash { top: 104px; left: 10px; width: 190px; height: 124px; }
  .sachet .badge { left: auto; right: 22px; top: 124px; width: 80px; height: 80px; border-width: 3px; }
  .sachet .badge__name { font-size: 14px; }

  .tags { position: absolute; top: 670px; left: 830px; display: flex; gap: 14px; }
  .tag { width: 70px; height: 70px; border-radius: 50%; border: 3px solid var(--white);
         box-shadow: 0 1px 6px rgba(60,40,30,.2); display: flex; align-items: center; justify-content: center;
         text-align: center; font-family: "Courgette", cursive; font-size: 12px; line-height: 1.05; color: var(--white); }
  .tag--bloom { background: var(--bloom-badge); }
  .tag--gold { background: var(--gold-badge); }
  .tag--brand { background: var(--white); color: var(--band); font-family: "Roboto Condensed", sans-serif; font-size: 11px; }
</style>
</head>
<body>
<main class="canvas">

  <section class="panel panel--side flavour--gold" aria-label="Velmora Gold box side panel">
    <p class="side__intro">Slow blended from whole cardamom, cinnamon, ginger and clove over a bold black tea base for a warm, rounded cup.</p>
    <div class="band side__band">
      <h3 class="side__heading">Reasons Tea Is Good for You</h3>
      <p class="side__sub">Our daily ritual for body and mind</p>
    </div>
    <div class="side__body">
      <p>Tea is naturally rich in antioxidants that help protect the body every day. Warming spices like ginger and cinnamon support easy digestion, while cardamom and clove lend comfort and calm. Each cup is made with no artificial flavours or preservatives, only whole leaves and spices.</p>
      <p>Add hot water to the teabag and steep for five to seven minutes. Finish with milk and your choice of sweetener, then enjoy. See the inside panel for full brewing steps.</p>
    </div>
  </section>

  <section class="panel panel--front-gold flavour--gold" aria-label="Velmora Gold box front panel">
    <div class="stripe stripe--left"></div>
    <div class="stripe stripe--right"></div>
    <div class="brand-mark"><span class="brand-mark__dot"></span>Velmora Leaf</div>
    <div class="band">
      <h1 class="band__name">Velmora Leaf</h1>
      <p class="band__tagline">Small Batch Chai Blends</p>
    </div>
    <div class="splash" role="img" aria-label="Splash of amber black chai tea"></div>
    <div class="badge"><span class="badge__name">Velmora<br>Gold</span><span class="badge__count">18 teabags</span></div>
    <p class="net">54 g (1.9 OZ)<br>A Product Of Alberta, Canada.</p>
  </section>

  <section class="panel panel--front-bloom flavour--bloom" aria-label="Velmora Bloom box front panel">
    <div class="stripe stripe--left"></div>
    <div class="stripe stripe--right"></div>
    <div class="brand-mark"><span class="brand-mark__dot"></span>Velmora Leaf</div>
    <div class="band">
      <h2 class="band__name">Velmora Leaf</h2>
      <p class="band__tagline">Small Batch Chai Blends</p>
    </div>
    <div class="splash" role="img" aria-label="Splash of pale green rooibos chai tea"></div>
    <div class="badge"><span class="badge__name">Velmora<br>Bloom</span><span class="badge__count">18 teabags</span></div>
    <p class="net">54 g (1.9 OZ)<br>A Product Of Alberta, Canada.</p>
  </section>

  <section class="sachet sachet--bloom flavour--bloom" aria-label="Velmora Bloom teabag sachet">
    <div class="stripe stripe--right"></div>
    <div class="brand-mark"><span class="brand-mark__dot"></span>Velmora Leaf</div>
    <div class="band">
      <p class="band__name">Velmora Leaf</p>
      <p class="band__tagline">Small Batch Chai Blends</p>
    </div>
    <div class="splash" role="img" aria-label="Splash of pale green rooibos chai tea"></div>
    <div class="badge"><span class="badge__name">Velmora<br>Bloom</span></div>
  </section>

  <section class="sachet sachet--gold flavour--gold" aria-label="Velmora Gold teabag sachet">
    <div class="stripe stripe--right"></div>
    <div class="brand-mark"><span class="brand-mark__dot"></span>Velmora Leaf</div>
    <div class="band">
      <p class="band__name">Velmora Leaf</p>
      <p class="band__tagline">Small Batch Chai Blends</p>
    </div>
    <div class="splash" role="img" aria-label="Splash of amber black chai tea"></div>
    <div class="badge"><span class="badge__name">Velmora<br>Gold</span></div>
  </section>

  <div class="tags" aria-label="Teabag string tags">
    <div class="tag tag--bloom">Velmora<br>Bloom</div>
    <div class="tag tag--gold">Velmora<br>Gold</div>
    <div class="tag tag--brand">Velmora<br>Leaf</div>
  </div>

</main>
</body>
</html>
```